The Book Cover for "Embracing the Quiet Lantern of Dawn" needs redesigned

First the back ground or art work needs to be replaced or redesigned.
The title Embracing the Quiet Lantern of Dawn needs to be redesigned so that the words "Discovering the" is diminished in size compared to the rest of the title "Quiet Lantern of Dawn"
The Sub-title "Tracing the silent journey of the Wandering Flame" needs to be more pronounced and readable.
The authors name needs to be downsized.

```html
<!DOCTYPE html>
<html lang="en">
<head>
<meta charset="utf-8">
<title>Embracing the Quiet Lantern of Dawn — Book Cover</title>
<link rel="stylesheet" href="https://fonts.googleapis.com/css2?family=Poppins:wght@600;700;800;900&display=swap">
<style>
  :root {
    --page: #ffffff;
    --night: #121f3a;
    --dusk: #22406a;
    --ember: #b8664a;
    --amber-sky: #f0b865;
    --horizon: #f9dca0;
    --cream: #fbf1dc;
    --amber: #f2a33a;
    --ink-navy: #16264a;
  }
  * { margin: 0; padding: 0; box-sizing: border-box; }
  html, body {
    width: 1200px;
    height: 1200px;
    overflow: hidden;
    background: var(--page);
  }
  .canvas {
    position: relative;
    width: 1200px;
    height: 1200px;
    background: var(--page);
    font-family: "Poppins", sans-serif;
  }
  .cover {
    position: absolute;
    left: 263px;
    top: 38px;
    width: 754px;
    height: 1131px;
    overflow: hidden;
  }
  .cover-sky {
    position: absolute;
    inset: 0;
    background: linear-gradient(to bottom,
      var(--night) 0%,
      var(--dusk) 55%,
      var(--ember) 78%,
      var(--amber-sky) 90%,
      var(--horizon) 100%);
  }
  .cover-art {
    position: absolute;
    left: 0;
    right: 0;
    bottom: 0;
    height: 420px;
    background: radial-gradient(ellipse 320px 220px at 50% 78%, rgba(255,240,200,0.9), rgba(255,240,200,0) 72%);
  }
  .title-art {
    position: absolute;
    left: 0;
    top: 0;
    width: 754px;
    height: 1131px;
  }
  .title-lead { fill: var(--amber); font-weight: 700; }
  .title-rule { stroke: var(--amber); stroke-width: 2; }
  .title-cream { fill: var(--cream); font-weight: 900; }
  .title-amber { fill: var(--amber); font-weight: 900; }
  .title-of { fill: var(--cream); font-weight: 700; }
  .subtitle-rule {
    position: absolute;
    left: 337px;
    top: 676px;
    width: 80px;
    height: 3px;
    background: var(--amber);
  }
  .subtitle {
    position: absolute;
    left: 0;
    width: 754px;
    top: 694px;
    text-align: center;
    color: var(--cream);
    font-weight: 700;
    font-size: 36px;
    line-height: 46px;
  }
  .author-name {
    position: absolute;
    left: 0;
    width: 754px;
    top: 1068px;
    text-align: center;
    color: var(--ink-navy);
    font-weight: 600;
    font-size: 18px;
    letter-spacing: 0.32em;
    padding-left: 0.32em;
    text-transform: uppercase;
  }
</style>
</head>
<body>
<div class="canvas">
  <section class="cover">
    <div class="cover-sky"></div>
    <div class="cover-art" role="img" aria-label="Illustration of a small lantern glowing on a hilltop at dawn"></div>

    <svg class="title-art" viewBox="0 0 754 1131" aria-label="Embracing the Quiet Lantern of Dawn">
      <line class="title-rule" x1="80" y1="108" x2="170" y2="108"/>
      <text class="title-lead" x="377" y="118" font-size="30" text-anchor="middle" textLength="380" lengthAdjust="spacing">EMBRACING THE</text>
      <line class="title-rule" x1="584" y1="108" x2="674" y2="108"/>
      <text class="title-cream" x="377" y="272" font-size="160" text-anchor="middle" textLength="560" lengthAdjust="spacingAndGlyphs">QUIET</text>
      <text class="title-amber" x="377" y="422" font-size="150" text-anchor="middle" textLength="600" lengthAdjust="spacingAndGlyphs">LANTERN</text>
      <text class="title-of" x="377" y="482" font-size="40" text-anchor="middle">OF</text>
      <text class="title-cream" x="377" y="640" font-size="170" text-anchor="middle" textLength="560" lengthAdjust="spacingAndGlyphs">DAWN</text>
    </svg>

    <div class="subtitle-rule"></div>
    <p class="subtitle">Tracing the Silent Journey<br>of the Wandering Flame</p>

    <p class="author-name">RT Jack Harrowgate</p>
  </section>
</div>
</body>
</html>
```